Design of a chocolate packaging

In hand-lettering-style: "Thank you for your work - you are an important part of our team!" (in big letters - almost 2/3 of the whole place) "This chocolate is a lot, so you enter into a raffle and have a great chance of a Zelta Rovo and many more great winnings ... all the information is below www.brv-nordlichtwerk.de! Good luck !!! " (in small letters underneath) The place is: 7,3cm * 15,3cm (crosswise)

Font styles to use
Script

```html
<!DOCTYPE html>
<html lang="de">
<head>
<meta charset="utf-8">
<title>Schokoladen-Banderolen – Weihnachten</title>
<link rel="stylesheet" href="https://fonts.googleapis.com/css2?family=Italianno&family=Playfair+Display:ital,wght@1,700&family=Josefin+Sans:wght@400&family=Lora:ital@1&display=swap">
<style>
  :root {
    --page-bg: #ffffff;
    --cocoa-deep: #2a0c05;
    --cocoa-mid: #5a2612;
    --cocoa-light: #7a3a1c;
    --caramel: #c08a5c;
    --caramel-light: #dcae80;
    --gold-text: #c79465;
  }
  * { margin: 0; padding: 0; box-sizing: border-box; }
  html, body { width: 1200px; height: 1200px; overflow: hidden; background: var(--page-bg); }
  .sheet { position: relative; width: 1200px; height: 1200px; }
  .wrapper {
    position: absolute; left: 321px; width: 560px; height: 270px; overflow: hidden;
    background: linear-gradient(160deg, var(--cocoa-deep) 0%, var(--cocoa-mid) 38%, var(--cocoa-light) 55%, var(--cocoa-mid) 72%, var(--cocoa-deep) 100%);
  }
  .wrapper--friend { top: 66px; }
  .wrapper--staff { top: 449px; }
  .wrapper--newyear { top: 854px; }
  .wrapper__silk, .wrapper__wave { position: absolute; inset: 0; width: 100%; height: 100%; }
  .greeting { position: absolute; font-family: "Italianno", cursive; color: var(--gold-text); line-height: 1; transform: rotate(-2deg); }
  .greeting--frohe { left: 110px; top: 26px; font-size: 72px; }
  .greeting--weihnachten { left: 30px; top: 90px; font-size: 80px; }
  .message {
    position: absolute; left: 320px; width: 230px; top: 44px; text-align: center;
    font-family: "Playfair Display", serif; font-style: italic; font-weight: 700;
    color: var(--cocoa-light); font-size: 22px; line-height: 24px;
    transform: rotate(-4deg); text-shadow: 0 1px 0 rgba(220,170,120,.45);
  }
  .wrapper--staff .message { left: 300px; width: 270px; top: 30px; line-height: 23px; }
  .wrapper--newyear .message { left: 340px; top: 40px; font-size: 28px; line-height: 30px; color: var(--caramel); }
  .raffle {
    position: absolute; left: 250px; width: 290px; top: 192px; text-align: center;
    font-family: "Lora", serif; font-style: italic; font-size: 9.6px; line-height: 12.4px; color: var(--gold-text);
  }
  .site {
    position: absolute; left: 30px; top: 236px;
    font-family: "Josefin Sans", sans-serif; font-size: 12.5px; letter-spacing: 2.2px; color: var(--gold-text);
  }
</style>
</head>
<body>
<main class="sheet">
  <section class="wrapper wrapper--friend">
    <svg class="wrapper__silk" viewBox="0 0 560 270" role="img" aria-label="Draped chocolate-brown silk background">
      <defs>
        <linearGradient id="silk" x1="0" y1="0" x2="1" y2="1">
          <stop offset="0" stop-color="#2a0c05" stop-opacity=".7"/>
          <stop offset=".5" stop-color="#8a4a26" stop-opacity=".35"/>
          <stop offset="1" stop-color="#2a0c05" stop-opacity=".7"/>
        </linearGradient>
      </defs>
      <rect width="560" height="270" fill="url(#silk)"/>
    </svg>
    <svg class="wrapper__wave" viewBox="0 0 560 270" aria-hidden="true">
      <path d="M0 200 C120 235 250 215 360 175 C440 148 510 150 560 175 L560 270 L0 270 Z" fill="#a8683c"/>
      <path d="M0 208 C120 240 250 222 360 184 C440 158 510 162 560 190 L560 270 L0 270 Z" fill="#2e0e06"/>
      <path d="M0 208 C120 240 250 222 360 184 C440 158 510 162 560 190" fill="none" stroke="#dcae80" stroke-width="1.5" opacity=".8"/>
    </svg>
    <div class="greeting greeting--frohe">Frohe</div>
    <div class="greeting greeting--weihnachten">Weihnachten</div>
    <p class="message">Danke<br>für Deine<br>Freundschaft!</p>
    <p class="raffle">Diese Schokolade ist ein Los.<br>Du nimmst damit an einer Verlosung<br>Teil und hast großartige Chancen auf einen Zelta Rovo<br>und viele weitere tolle Gewinne...alle Infos gibt es<br>unter www.brv-nordlichtwerk.de! Viel Glück!!!</p>
    <p class="site">www.brv-nordlichtwerk.de</p>
  </section>

  <section class="wrapper wrapper--staff">
    <svg class="wrapper__silk" viewBox="0 0 560 270" role="img" aria-label="Draped chocolate-brown silk background">
      <rect width="560" height="270" fill="url(#silk)"/>
    </svg>
    <svg class="wrapper__wave" viewBox="0 0 560 270" aria-hidden="true">
      <path d="M0 200 C120 235 250 215 360 175 C440 148 510 150 560 175 L560 270 L0 270 Z" fill="#a8683c"/>
      <path d="M0 208 C120 240 250 222 360 184 C440 158 510 162 560 190 L560 270 L0 270 Z" fill="#2e0e06"/>
      <path d="M0 208 C120 240 250 222 360 184 C440 158 510 162 560 190" fill="none" stroke="#dcae80" stroke-width="1.5" opacity=".8"/>
    </svg>
    <div class="greeting greeting--frohe">Frohe</div>
    <div class="greeting greeting--weihnachten">Weihnachten</div>
    <p class="message">Danke für ein Jahr<br>wertvoller Mitarbeit<br>in unserem<br>Unternehmen</p>
    <p class="raffle">Diese Schokolade ist ein Los.<br>Du nimmst damit an einer Verlosung<br>Teil und hast großartige Chancen auf einen Zelta Rovo<br>und viele weitere tolle Gewinne...alle Infos gibt es<br>unter www.brv-nordlichtwerk.de! Viel Glück!!!</p>
    <p class="site">www.brv-nordlichtwerk.de</p>
  </section>

  <section class="wrapper wrapper--newyear">
    <svg class="wrapper__silk" viewBox="0 0 560 270" role="img" aria-label="Draped chocolate-brown silk background">
      <rect width="560" height="270" fill="url(#silk)"/>
    </svg>
    <svg class="wrapper__wave" viewBox="0 0 560 270" aria-hidden="true">
      <path d="M0 200 C120 235 250 215 360 175 C440 148 510 150 560 175 L560 270 L0 270 Z" fill="#a8683c"/>
      <path d="M0 208 C120 240 250 222 360 184 C440 158 510 162 560 190 L560 270 L0 270 Z" fill="#2e0e06"/>
      <path d="M0 208 C120 240 250 222 360 184 C440 158 510 162 560 190" fill="none" stroke="#dcae80" stroke-width="1.5" opacity=".8"/>
    </svg>
    <div class="greeting greeting--frohe">Frohe</div>
    <div class="greeting greeting--weihnachten">Weihnachten</div>
    <p class="message">Alles Gute<br>für 2019...</p>
    <p class="raffle">Diese Schokolade ist ein Los.<br>Du nimmst damit an einer Verlosung<br>Teil und hast großartige Chancen auf einen Zelta Rovo<br>und viele weitere tolle Gewinne...alle Infos gibt es<br>unter www.brv-nordlichtwerk.de! Viel Glück!!!</p>
    <p class="site">www.brv-nordlichtwerk.de</p>
  </section>
</main>
</body>
</html>
```